Custom Business Card Design

We are looking for a raised spot logo design to use with Plinkory.com. We will provide the logo files. Should be a front and back design. We want to implement the house into the back design using the same colors as the logo through out. Something VERY cool!

Industry/Entity Type

Business

```html
<!DOCTYPE html>
<html lang="en">
<head>
<meta charset="utf-8">
<title>Plinkory Business Card – Front and Back</title>
<link href="https://fonts.googleapis.com/css2?family=Montserrat:wght@400;500;600&display=swap" rel="stylesheet">
<style>
  :root {
    --page: #eef3f8;
    --card-black: #050505;
    --brand-blue: #3476bb;
    --brand-red: #e8474c;
    --text-muted: #8fa8c4;
    --divider: #3b3b3b;
  }
  * { box-sizing: border-box; margin: 0; padding: 0; }
  html, body { width: 1200px; height: 750px; overflow: hidden; }
  body {
    background: var(--page);
    font-family: "Montserrat", sans-serif;
    position: relative;
  }
  .card {
    position: absolute;
    top: 235px;
    width: 490px;
    height: 280px;
    border-radius: 24px;
    background: var(--card-black);
    overflow: hidden;
    box-shadow: 0 12px 30px rgba(0,0,0,0.25);
  }
  .card--front { left: 80px; }
  .card--back { left: 630px; }

  .brand-name {
    display: flex;
    align-items: center;
    gap: 8px;
    color: var(--brand-blue);
    font-weight: 600;
    letter-spacing: 0.5px;
  }
  .brand-name::before {
    content: "";
    width: 12px;
    height: 12px;
    border-radius: 50%;
    background: var(--brand-blue);
  }
  .card--front .brand-name {
    position: absolute;
    left: 52px;
    top: 118px;
    font-size: 34px;
  }
  .card--back .brand-name {
    position: absolute;
    right: 34px;
    top: 34px;
    font-size: 26px;
  }

  .details {
    position: absolute;
    left: 24px;
    right: 20px;
    top: 138px;
    display: flex;
    align-items: center;
  }
  .person {
    flex: none;
    padding-right: 12px;
    margin-right: 12px;
    border-right: 1px solid var(--divider);
  }
  .person__name {
    font-size: 17px;
    font-weight: 500;
    color: var(--brand-blue);
    letter-spacing: 0.2px;
    white-space: nowrap;
  }
  .person__name .surname { color: var(--brand-red); }
  .person__role {
    font-size: 9.5px;
    color: var(--brand-blue);
    letter-spacing: 0.8px;
    margin-top: 3px;
  }

  .contacts {
    display: grid;
    grid-template-columns: auto auto;
    column-gap: 10px;
    row-gap: 6px;
    font-size: 8.5px;
    color: var(--text-muted);
  }
  .contact { display: flex; align-items: center; gap: 5px; white-space: nowrap; }
  .contact__icon {
    flex: none;
    width: 12px; height: 12px;
    background: var(--brand-red);
    border-radius: 2px;
    display: flex; align-items: center; justify-content: center;
  }
  .contact__icon svg { width: 8px; height: 8px; }

  .company-band {
    position: absolute;
    left: 0; right: 0; bottom: 14px;
    height: 56px;
    background: var(--brand-blue);
    padding: 11px 30px;
    color: #ffffff;
  }
  .company-band__name { font-size: 12px; font-weight: 600; letter-spacing: 0.5px; }
  .company-band__address { font-size: 11px; letter-spacing: 0.3px; margin-top: 3px; }
  .accent-band {
    position: absolute;
    left: 0; right: 0; bottom: 0;
    height: 14px;
    background: var(--brand-red);
  }
</style>
</head>
<body>

  <section class="card card--front" aria-label="Card front">
    <div class="brand-name">Plinkory</div>
  </section>

  <section class="card card--back" aria-label="Card back">
    <div class="brand-name">Plinkory</div>

    <div class="details">
      <div class="person">
        <div class="person__name">MARTEN<span class="surname">CALLOWAY</span></div>
        <div class="person__role">CREATIVE DIRECTOR</div>
      </div>

      <div class="contacts">
        <div class="contact">
          <span class="contact__icon"><svg viewBox="0 0 10 10"><path d="M2 1h2l1 2-1 1a5 5 0 0 0 2 2l1-1 2 1v2c-4 1-8-3-7-7z" fill="#fff"/></svg></span>
          +49 211 58302-0
        </div>
        <div class="contact">
          <span class="contact__icon"><svg viewBox="0 0 10 10"><circle cx="5" cy="5" r="3.6" fill="none" stroke="#fff" stroke-width="1.2"/><path d="M1.5 5h7M5 1.5v7" stroke="#fff" stroke-width="0.9"/></svg></span>
          www.plinkory.com
        </div>
        <div class="contact">
          <span class="contact__icon"><svg viewBox="0 0 10 10"><rect x="2" y="3" width="6" height="4" fill="#fff"/><rect x="3" y="1.5" width="4" height="2" fill="none" stroke="#fff"/></svg></span>
          +49 211 58302-4
        </div>
        <div class="contact">
          <span class="contact__icon"><svg viewBox="0 0 10 10"><rect x="1.5" y="2.5" width="7" height="5" fill="none" stroke="#fff"/><path d="M1.5 2.5l3.5 3 3.5-3" fill="none" stroke="#fff"/></svg></span>
          marten@plinkory.com
        </div>
        <div class="contact">
          <span class="contact__icon"><svg viewBox="0 0 10 10"><rect x="3" y="1" width="4" height="8" rx="0.8" fill="none" stroke="#fff"/></svg></span>
          +49 352 8174 65
        </div>
      </div>
    </div>

    <div class="company-band">
      <div class="company-band__name">PLINKORY LIMITED</div>
      <div class="company-band__address">BRELLINGER STRASSE-214 40593 DÜSSELDORF, USA</div>
    </div>
    <div class="accent-band"></div>
  </section>

</body>
</html>
```